PowerPoint Design for a Biotech Consulting Firm

We need a powerpoint design for a new business based in Philadelphia called VorentaRx. This is a consulting firm that will serve medical diagnostics industry, which is part of the life science/healthcare industry focusing on developing and marketing products that help in early detection, monitoring or management of diseases. Our consulting firm will help medical diagnostic companies to overcome key challenges in designing, evaluating and marketing new products.Our company name is VorentaRx. Vorenta is Latin word for "something", Dx represents diagnostics. The idea behind the name is that we help companies to transform the original, early product ideas ("nothing") into "something" which is a product with full clinical utility that will help to improve health and well-being.The powerpoint should use the visual feel of the logo (attached), be modern, simple and clean looking and represent creativity, innovation, scientific thinking and progress.

Target Market(s)

Biotech

Industry/Entity Type

Biotechnology

Font styles to use
Sans Serif

Colors
0355a3
3276b5
85abd2
cfdeed
ffffff
959595
aaaaaa
cbcbcb
070707

Requirements
Must have
• - look and feel, logo colors
• - multiple slide formats

```html
<!DOCTYPE html>
<html lang="en">
<head>
<meta charset="utf-8">
<title>VorentaRx – Introduction</title>
<link href="https://fonts.googleapis.com/css2?family=Jost:wght@300;400;500&display=swap" rel="stylesheet">
<style>
  :root {
    --brand-blue: #2f8ef7;
    --ink: #1a1a1a;
    --paper: #ffffff;
  }
  * { margin: 0; padding: 0; box-sizing: border-box; }
  html, body {
    width: 1200px; height: 675px; overflow: hidden;
    background: var(--paper);
  }
  .slide {
    position: relative; width: 1200px; height: 675px;
    background: var(--paper);
    font-family: "Jost", "Futura", sans-serif;
    color: var(--ink);
    overflow: hidden;
  }
  .rule { position: absolute; background: var(--brand-blue); }
  .rule--top { left: 194px; top: 39px; width: 1006px; height: 9px; }
  .rule--right { left: 1133px; top: 0; width: 9px; height: 626px; }
  .rule--bottom { left: 58px; top: 626px; width: 1085px; height: 10px; }

  .brand-name {
    position: absolute; left: 34px; top: 84px; width: 150px;
    font-weight: 500; font-size: 22px; line-height: 28px;
    color: var(--ink); letter-spacing: 0.2px;
  }

  .slide__title {
    position: absolute; left: 203px; top: 104px;
    font-weight: 300; font-size: 62px; line-height: 1;
    letter-spacing: -0.5px; color: var(--ink);
  }

  .points { position: absolute; left: 207px; top: 201px; width: 880px; list-style: none; }
  .points__item {
    position: relative; padding-left: 21px;
    font-weight: 300; font-size: 29.5px; line-height: 31px;
    margin-bottom: 60px;
  }
  .points__item::before {
    content: ""; position: absolute; left: 0; top: 12px;
    width: 8px; height: 8px; background: var(--ink);
  }

  .tag {
    position: absolute; top: 569px; height: 38px;
    background: var(--brand-blue); color: var(--paper);
    font-size: 14px; font-weight: 300;
    display: flex; align-items: center;
  }
  .tag--date { left: 11px; width: 116px; padding-left: 10px; }
  .tag--page { left: 138px; width: 56px; justify-content: flex-end; padding-right: 10px; }

  .copyright {
    position: absolute; left: 728px; top: 626px; width: 405px; height: 25px;
    background: var(--brand-blue); color: var(--paper);
    font-size: 15px; font-weight: 300;
    display: flex; align-items: center; justify-content: center;
  }
</style>
</head>
<body>
<main class="slide">
  <div class="rule rule--top"></div>
  <div class="rule rule--right"></div>
  <div class="rule rule--bottom"></div>

  <div class="brand-name">VorentaRx</div>

  <h1 class="slide__title">INTRODUCTION</h1>

  <ul class="points">
    <li class="points__item">Lorem ipsum dolor sit amet, consectetur adipiscing elit, sed do eiusmod tempor incididunt ut labore et dolore magna aliqua.</li>
    <li class="points__item">Lorem ipsum dolor sit amet, consectetur adipiscing elit, sed do eiusmod tempor incididunt ut labore et dolore magna aliqua.</li>
    <li class="points__item">Lorem ipsum dolor sit amet, consectetur adipiscing elit, sed do eiusmod tempor incididunt ut labore et dolore magna aliqua.</li>
  </ul>

  <div class="tag tag--date">6/15/2019</div>
  <div class="tag tag--page">2</div>
  <div class="copyright">Copyright 2019-2020</div>
</main>
</body>
</html>
```